Need App for Impact Related Events

My app is to help with internal events. When you enter the prompted event code the next screen shows you everyone currently at the event. It will give you the ability to Start a conversation with someone you met at that event, or signal it is your turn to send a message. The next screen is a message thread with that person. I am looking for a design that incorporates the colors and ‘feel good’ emotion of our logo. I have pieced together a pretty good interpretation of what I’m looking for in the attached mockup by slicing and dicing designs. I also attached our logo mascot.Screens (see attached mockups)

Note 1: I do not like the picture on the screen used in screen one because it makes it seem like a dating app. I attached an alternative photo that can be used or present different ideas.

Note 2: On the login/signup screen (screen 2) I need an additional first and last name for login, you can try to fit this on one login screen or present a two step signup screen where that is presented in the second screen.

READ MOCKUP GUIDELINES UNDER Must Haves

Target Market(s)

People attending internal social impact events

Industry/Entity Type

Charity

Font styles to use
Sans Serif

Colors
86cfc6

Requirements
Must have
• Follow the screen mockups attached to project
• PLEASE READ
• I have provided a relatively close design of what I’m looking for in the mockups. Some screens need to be followed more closely to my design mockup than other. I have listed a guide below how how closely you should follow my mockup design exactly. Overall I would like to see some ideas of incorporating a few accent colors so it doesn’t appear SO Blue. I also attached some app inspiration designs I found from around the web
• Screen Mockup Guideline Follow %
• Screen 1: 65% - mostly on target, would like to see ways to make it not SO Blue and possibly creative places to add some explainer text describing the app
• Screen 2: 50% - general design idea is here, but more open
• Screen 3: 35% - a lot more room for design influence
• Screen 4: 70% - mostly on target, a little room for design influence/color scheme ideas
• Screen 5-6: 25% - a lot of room for design change/ideas/influence
• Screen 7-8: 80% - already very close to what I need, maybe open to slight sizing and color scheme ideas
• Screen 9: 15% - the most open for influence, only the general functionality of the screen is communicated here
Nice to have
• Please Read Mockup Guideline above. In large part I am looking for something to use some nice accent colors so it is not overwhelmingly blue and bring the whole design into a seamless style.
Should not have

```html
<!DOCTYPE html>
<html lang="en">
<head>
<meta charset="utf-8">
<title>Notifications</title>
<link href="https://fonts.googleapis.com/css2?family=Nunito+Sans:wght@400;600;700;800&display=swap" rel="stylesheet">
<style>
  :root {
    --bg: #ffffff;
    --ink: #262634;
    --ink-soft: #4a4a58;
    --muted: #8a8a96;
    --divider: #ececf0;
    --teal: #86cfc6;
    --teal-deep: #3fa89b;
    --avatar-tone: #7d7a78;
    --avatar-tone-light: #c9c5c1;
  }
  * { box-sizing: border-box; margin: 0; padding: 0; }
  html, body {
    width: 675px; height: 1200px; overflow: hidden;
    background: var(--bg);
    font-family: "Nunito Sans", sans-serif;
    color: var(--ink);
  }
  .screen { position: relative; width: 675px; height: 1200px; }

  .app-header {
    position: absolute; top: 28px; left: 29px; right: 30px;
    display: flex; justify-content: space-between; align-items: center;
  }
  .app-header h1 { font-size: 56px; font-weight: 800; letter-spacing: -0.3px; }
  .avatar {
    border-radius: 50%;
    background: radial-gradient(circle at 45% 40%, var(--avatar-tone-light), var(--avatar-tone));
  }
  .avatar--profile { width: 66px; height: 66px; }

  .section-title {
    position: absolute; top: 136px; left: 29px;
    font-size: 38px; font-weight: 800;
  }
  .divider { position: absolute; left: 0; right: 0; height: 2px; background: var(--divider); }
  .divider--top { top: 203px; }
  .divider--bottom { top: 354px; }

  .notification {
    position: absolute; top: 244px; left: 32px;
    display: flex; gap: 28px; align-items: flex-start;
  }
  .avatar--sender { width: 64px; height: 64px; flex: none; margin-top: 4px; }
  .notification__text { width: 470px; font-size: 26px; line-height: 34px; color: var(--ink-soft); }
  .notification__text strong { color: var(--ink); font-weight: 800; }
  .notification__time { display: block; margin-top: 6px; font-size: 17px; line-height: 20px; color: var(--muted); }

  .tab-bar {
    position: absolute; left: 0; right: 0; top: 1082px; height: 118px;
  }
  .tab-icon { position: absolute; top: 46px; width: 52px; height: 52px; }
  .tab-icon--calendar { left: 42px; }
  .tab-icon--chat { left: 176px; }
  .tab-icon--alerts { left: 444px; }
  .tab-icon--settings { left: 580px; }
  .tab-badge {
    position: absolute; left: 461px; top: 12px;
    width: 18px; height: 18px; border-radius: 50%; background: var(--teal-deep);
  }
  .add-button {
    position: absolute; left: 284px; top: 0; width: 106px; height: 106px;
    border-radius: 50%;
    background: linear-gradient(135deg, var(--teal-deep) 10%, var(--teal) 100%);
    display: flex; align-items: center; justify-content: center;
  }
</style>
</head>
<body>
<main class="screen">
  <header class="app-header">
    <h1>Notifications</h1>
    <div class="avatar avatar--profile" role="img" aria-label="Profile photo of the signed-in user"></div>
  </header>

  <h2 class="section-title">Today</h2>
  <div class="divider divider--top"></div>

  <article class="notification">
    <div class="avatar avatar--sender" role="img" aria-label="Profile photo of Marco Hale"></div>
    <p class="notification__text">
      <strong>Marco Hale</strong> and <strong>2 others</strong> will be<br>attending Nadia's Birthday
      <span class="notification__time">01:13</span>
    </p>
  </article>
  <div class="divider divider--bottom"></div>

  <nav class="tab-bar">
    <svg class="tab-icon tab-icon--calendar" viewBox="0 0 52 52" fill="none" stroke="#3fa89b" stroke-width="3.4" stroke-linecap="round">
      <rect x="6" y="9" width="40" height="37" rx="4"/>
      <line x1="6" y1="20" x2="46" y2="20"/>
      <line x1="16" y1="4" x2="16" y2="13"/>
      <line x1="36" y1="4" x2="36" y2="13"/>
    </svg>
    <svg class="tab-icon tab-icon--chat" viewBox="0 0 52 52" fill="none" stroke="#3fa89b" stroke-width="3.4" stroke-linejoin="round">
      <path d="M26 8a18 18 0 1 0 9 33.6L44 44l-2.6-8.6A18 18 0 0 0 26 8z"/>
    </svg>
    <div class="add-button" aria-label="Create event">
      <svg width="44" height="44" viewBox="0 0 44 44" stroke="#ffffff" stroke-width="4" stroke-linecap="round">
        <line x1="22" y1="6" x2="22" y2="38"/><line x1="6" y1="22" x2="38" y2="22"/>
      </svg>
    </div>
    <span class="tab-badge"></span>
    <svg class="tab-icon tab-icon--alerts" viewBox="0 0 52 52" fill="none" stroke="#3fa89b" stroke-width="3.4" stroke-linejoin="round" stroke-linecap="round">
      <path d="M26 6c-8 0-13 6-13 14v10l-5 8h36l-5-8V20c0-8-5-14-13-14z"/>
      <path d="M21 43a5 5 0 0 0 10 0"/>
    </svg>
    <svg class="tab-icon tab-icon--settings" viewBox="0 0 52 52" fill="none" stroke="#3fa89b" stroke-width="3.4" stroke-linecap="round">
      <line x1="4" y1="18" x2="48" y2="18"/>
      <line x1="4" y1="34" x2="48" y2="34"/>
      <circle cx="34" cy="18" r="5" fill="#3fa89b"/>
      <circle cx="17" cy="34" r="5" fill="#3fa89b"/>
    </svg>
  </nav>
</main>
</body>
</html>
```